Endocrinologist needs new stationery

I have a logo from MarkForge and now need stationery with the new logo.

Address: Suite 4, 282 Falcon Street, Hawthorn, VIC 3122
Phone: 03 9417 2253
Fax: 03 9417 2255
Website: www.drmaylacorwen.com.au
Email: admin@drmaylacorwen.com.au

```html
<!DOCTYPE html>
<html lang="en">
<head>
<meta charset="utf-8">
<title>Dr Mayla Corwen – Stationery</title>
<link href="https://fonts.googleapis.com/css2?family=Mulish:wght@300;400&family=Crimson+Text&display=swap" rel="stylesheet">
<style>
  :root {
    --sheet-bg: #cccccc;
    --paper: #ffffff;
    --ink-blue: #2f6fb8;
    --contact-blue: #3a63b0;
    --body-ink: #2b2b2b;
    --grad-blue: #2f78c8;
    --grad-mid: #3f62aa;
    --grad-purple: #573f78;
    --envelope-edge: #dde3e0;
  }
  * { box-sizing: border-box; margin: 0; padding: 0; }
  html, body { width: 849px; height: 1200px; overflow: hidden; }
  body {
    position: relative;
    background: var(--sheet-bg);
    font-family: "Mulish", Arial, sans-serif;
  }
  .label {
    position: absolute;
    font-family: "Crimson Text", Georgia, serif;
    font-size: 10px;
    color: #111;
    transform: translateX(-50%);
    white-space: nowrap;
  }
  .brand-name {
    font-family: "Mulish", Arial, sans-serif;
    font-weight: 300;
    color: var(--ink-blue);
    white-space: nowrap;
    letter-spacing: 0.02em;
  }
  .contact {
    position: absolute;
    display: flex;
    color: var(--contact-blue);
    font-weight: 400;
    white-space: nowrap;
  }
  .contact .divider {
    position: relative;
    width: 1px;
    background: var(--contact-blue);
  }
  .contact .divider::before,
  .contact .divider::after {
    content: "";
    position: absolute;
    left: -1px;
    width: 3px; height: 3px;
    border-radius: 50%;
    background: var(--contact-blue);
  }
  .contact .divider::before { top: -1px; }
  .contact .divider::after { bottom: -1px; }

  /* Letterhead */
  .letterhead {
    position: absolute;
    left: 147px; top: 29px;
    width: 555px; height: 718px;
    background: var(--paper);
  }
  .letterhead .side-band {
    position: absolute; left: 0; top: 0; bottom: 0;
    width: 24px;
    background: linear-gradient(to right, var(--grad-mid), var(--grad-purple));
  }
  .letterhead .brand-name { position: absolute; left: 61px; top: 36px; font-size: 21px; }
  .letterhead .contact { left: 53px; top: 76px; font-size: 6.8px; line-height: 8.8px; }
  .letterhead .contact .col-left { margin-right: 4px; }
  .letterhead .contact .col-right { margin-left: 4px; }
  .letterhead .headline {
    position: absolute; left: 53px; top: 157px;
    font-size: 21px; font-weight: 400; color: var(--ink-blue);
  }
  .letterhead .body-copy {
    position: absolute; left: 53px; top: 192px; width: 470px;
    font-size: 8.25px; line-height: 11.8px; color: var(--body-ink);
    text-align: justify;
  }
  .letterhead .body-copy p { margin-bottom: 11.8px; }

  /* Business cards */
  .card {
    position: absolute; top: 771px;
    width: 254px; height: 145px;
  }
  .card-front { left: 147px; background: var(--paper); }
  .card-back {
    left: 448px;
    background: linear-gradient(to right, var(--grad-blue), var(--grad-mid) 45%, var(--grad-purple));
  }
  .card-front .brand-name { position: absolute; left: 0; right: 0; top: 38px; text-align: center; font-size: 19px; }
  .card-front .contact { left: 28px; top: 86px; font-size: 7.8px; line-height: 9.9px; }
  .card-front .contact .col-left { margin-right: 4px; }
  .card-front .contact .col-right { margin-left: 4px; }
  .card-back .brand-name { position: absolute; left: 0; right: 0; top: 58px; text-align: center; font-size: 19px; color: #fff; }

  /* Envelopes */
  .envelope {
    position: absolute; top: 940px;
    width: 327px; height: 231px;
    background: var(--envelope-edge);
  }
  .envelope-front { left: 76px; }
  .envelope-back { left: 451px; }
  .envelope-front .face {
    position: absolute; left: 1px; top: 1px; right: 10px; bottom: 8px;
    background: linear-gradient(to bottom, #ffffff, #f5f6f6);
  }
  .envelope-front .brand-name { position: absolute; left: 25px; top: 19px; font-size: 10px; }
  .envelope-front .contact { left: 20px; top: 44px; font-size: 3.6px; line-height: 4.6px; }
  .envelope-front .contact .col-left { margin-right: 2px; }
  .envelope-front .contact .col-right { margin-left: 2px; }
  .envelope-back .face {
    position: absolute; left: 6px; top: 0; right: 10px; bottom: 8px;
    background: linear-gradient(to bottom, #f7f8f8, #e9eeec);
  }
  .envelope-back .flap { position: absolute; left: 0; top: 0; width: 327px; height: 64px; }
  .envelope-back .brand-name { position: absolute; left: 0; right: 0; top: 19px; text-align: center; font-size: 10px; color: #e8ecf6; }
</style>
</head>
<body>

  <div class="label" style="left:424px; top:11px;">Letterhead</div>
  <section class="letterhead">
    <div class="side-band"></div>
    <div class="brand-name">Dr Mayla Corwen</div>
    <div class="contact">
      <div class="col-left">Phone: 03 9417 2253<br>Fax: 03 9417 2255<br>admin@drmaylacorwen.com.au</div>
      <div class="divider"></div>
      <div class="col-right">Suite 4, 282 Falcon Street,<br>Hawthorn, VIC 3122<br>www.drmaylacorwen.com.au</div>
    </div>
    <h1 class="headline">Headline</h1>
    <div class="body-copy">
      <p>Elendel ipsant, sincti verspic teceptatum arum et audis ex enit quideri busdam, core por aut aut a cusdae omnistiori dolutas molupta vendam, quas seque pora dolorepudis dollab ipsa volore velibus voluptatur ressim ius ut lanimol enihilique porios enet quas accusdae prae nullupta perum resentur, simusci ut occatatur? Cia platur?</p>
      <p>Dae sit alis eumquist aut liciendae vent a con nectur ad et ipictur maio es es ea volupta ecerum que ped quiatures quiatiis eseque voluptat omnihil laboris velenitatur, num quamustin pratiis qui ulparis dit modigentur as autatur, es sitate con pos volessi tassin es dolorit voluptasped quunt occupta tiuntisquis pratias eatur atatemped magnit provid quaecerum estibea sunt ipisci a preceribea deliasit officilit mos sequia culpariam ad ma vides exerumque paribus aria quo to di incitas piciusciis aliquam erovid que nonsequo de nam, officae porro te nossit et untio. Nectatia dolut lanis recupta tiundam quatusamus explique premporit mo moluptatum nus rest, temquodites volora exerovitatur seritae ma corum restrumqui rem doluptur si sitat.</p>
      <p>Si consed qui qui doluptas exerovidusa num et, cum vid ut etur aborehent voles et quae volores trumquis poremporro ex et iuscitatia atio quam quossim facid mosam eiur?</p>
      <p>Tat reperitis dolupti odionsequate porrorest, od ut fugias dolupta ad maximende rerupita velendigenda cus est es nimin culliquam harum reius que pro odigendipsa doloris adiantu rerrume niant.</p>
      <p>Unt mo quid mos rendae apiendae sandandi omnimus asperum rectas dolo ex et, si ut volestia num erchicia inveliqui rem quis estempori accumqu idellam ius enduntiunt.<br>Icid eri to voluptatur alitae est enditate soluptatium velecus.</p>
      <p>Is es re nitatibusam, simpel et endebitati ulparch ilicius reiunt ea nonest, consed ma quo mi, comnimendi occaerum descia dolupta eprovidendae dolo blabo. Ehendaeped quis es dus, tecturestius volut ulparum am ut qui dolorum et perehen tiaspid usdamus, nem autatem dolutat.</p>
      <p>Am, andae non explic temquam quam quam fugiasincil ius esequodis volorit ut explita tempor magnimu stiunt labo. Nem consed et fugiae. Itae cus. Ilite cusdam, sit quis elest ea vello velicta prehendis dit, quam es explitat eseque cust, quos idest pra perunt as ut aut fuga. Officiuntur rem lauditibus es exersperae nimus eos as asperiost od et latem sequi omni quia eum re pro est, iur res et verum ipsapid es aut officiatur?</p>
      <p>Ota ventium enditati ditas non pre veri tem doluptasin res plaborerum ut facium estio verovid quideniae. Et autatem et unt ad et magnatemque esti reptat.<br>Il illabore pero teces earuptur? Omnihilit qui di nonsequos et officia nos quatemosa dellant pliatissunt, ipiendi aut ut moloribus modi tet laboris nonsequam ratust, omnitinciur? Ferspiet, nulparione con rerumet autem experum aborrum demporum et omnimet doleste mperunt estis simusci endemporem ea quasperciis apedi iunt explam sit vite perumquam et et eos eos magnihil es et perspis aut qui reped ut occus atus. Latiorrum untotat am quiam seque porit essit ut pratio. Dantia nestrumquo expel ius provit, eate esequuntia perum hilic torem iur, tem. Nam ut audae nissunt doleceperum ullitat.</p>
      <p>Ga. Et ommolor eperrovidit ent. Qui occatustium qui recati ut rende sit quossequaes simod quam idis sintia dis velenem aces et ut accusap elluptum il estrum restetus doluptates sum ratquo tem faccull uptiuscitis enis sam imaximperia dolupid untempe llignihit vent es doluptatur aliquis quosam exerspis doluptatiis maximus debis aliquae velibus rerferi consecabo.</p>
    </div>
  </section>

  <div class="label" style="left:275px; top:751px;">Business card front</div>
  <div class="label" style="left:575px; top:751px;">Business card back</div>
  <section class="card card-front">
    <div class="brand-name">Dr Mayla Corwen</div>
    <div class="contact">
      <div class="col-left">Phone: 03 9417 2253<br>Fax: 03 9417 2255<br>admin@drmaylacorwen.com.au</div>
      <div class="divider"></div>
      <div class="col-right">Suite 4, 282 Falcon Street,<br>Hawthorn, VIC 3122<br>www.drmaylacorwen.com.au</div>
    </div>
  </section>
  <section class="card card-back">
    <div class="brand-name">Dr Mayla Corwen</div>
  </section>

  <div class="label" style="left:234px; top:920px;">C5 Envelope front</div>
  <div class="label" style="left:609px; top:920px;">C5 Envelope back</div>
  <section class="envelope envelope-front">
    <div class="face">
      <div class="brand-name">Dr Mayla Corwen</div>
      <div class="contact">
        <div class="col-left">Phone: 03 9417 2253<br>Fax: 03 9417 2255<br>admin@drmaylacorwen.com.au</div>
        <div class="divider"></div>
        <div class="col-right">Suite 4, 282 Falcon Street,<br>Hawthorn, VIC 3122<br>www.drmaylacorwen.com.au</div>
      </div>
    </div>
  </section>
  <section class="envelope envelope-back">
    <div class="face"></div>
    <svg class="flap" viewBox="0 0 327 64" aria-hidden="true">
      <defs>
        <linearGradient id="flapGradient" x1="0" y1="0" x2="1" y2="0">
          <stop offset="0" stop-color="#3b67b0"/>
          <stop offset="0.5" stop-color="#4c4f8e"/>
          <stop offset="0.85" stop-color="#3f62aa"/>
          <stop offset="1" stop-color="#2f78c8"/>
        </linearGradient>
      </defs>
      <path d="M2 0 H316 L297 56 Q294 63 286 63 H29 Q21 63 18 56 Z" fill="url(#flapGradient)"/>
    </svg>
    <div class="brand-name">Dr Mayla Corwen</div>
  </section>

</body>
</html>
```